Waterproofing Adhesive company needs design for bucket

We need a design for our 20kg/15kg and 4 kg bucket, Our companys name is Zorvane Co LLC based in Umm Al Quwain, United Arab Emirates . Our main business is into waterproofing paint and Adhesive manufacturing. We are looking for a creative design for our buckets and paper bags. The design have to be attractive, The color theme of our company is light orange and yellow. I have attached the company logo along with this.

Target Market(s)

B2b , construction companys
Maintenance company

Industry/Entity Type

Manufacturer

Requirements
Must have
• It must have the company logo
• a spcae in centre to write the different products names
Nice to have
• A attractive design for placing the bucket in retail shops

```html
<!DOCTYPE html>
<html lang="en">
<head>
<meta charset="utf-8">
<title>Zorvane Co LLC – Bucket Label</title>
<link rel="stylesheet" href="https://fonts.googleapis.com/css2?family=Anton&family=Archivo+Black&family=Roboto+Condensed:wght@700&display=swap">
<style>
  :root{
    --page:#e4e4e4;
    --label:#f4f4f4;
    --charcoal:#2f2f2f;
    --red:#c0262c;
    --orange:#e8862a;
    --amber:#eaa52f;
    --yellow:#f2dc1e;
    --rust:#b4460c;
    --white:#ffffff;
  }
  *{margin:0;padding:0;box-sizing:border-box}
  html,body{width:1200px;height:1026px;overflow:hidden;background:var(--page)}
  .canvas{position:relative;width:1200px;height:1026px}
  .label-art{position:absolute;left:0;top:0}
  .tagline{
    position:absolute;left:452px;top:156px;width:680px;
    font-family:"Archivo Black",sans-serif;font-size:35px;line-height:1.05;letter-spacing:1px;
    color:var(--yellow);white-space:nowrap;
  }
  .brand{
    position:absolute;left:100px;top:660px;width:230px;
    font-family:"Roboto Condensed",sans-serif;font-weight:700;font-size:36px;line-height:1.05;
    color:var(--orange);text-align:right;
  }
  .product-name,.product-code{
    position:absolute;left:406px;font-family:"Anton",sans-serif;line-height:1;
    white-space:nowrap;transform-origin:left top;
  }
  .product-name{
    top:462px;font-size:116px;color:var(--amber);
    transform:scaleX(1.62);text-shadow:2px 3px 0 #3a2a1a;
  }
  .product-code{
    top:570px;font-size:121px;color:var(--rust);
    transform:scaleX(1.45);text-shadow:2px 3px 0 #2a1a10;
  }
  .website{
    position:absolute;left:428px;top:864px;width:354px;text-align:center;
    font-family:"Roboto Condensed",sans-serif;font-weight:700;font-size:29px;line-height:1;color:var(--white);
  }
  .net-weight{
    position:absolute;left:928px;top:776px;
    font-family:"Anton",sans-serif;font-size:84px;line-height:1;color:var(--amber);
    text-shadow:2px 2px 0 #1a1a1a;white-space:nowrap;
  }
  .net-weight small{font-size:44px}
</style>
</head>
<body>
<div class="canvas">
  <svg class="label-art" width="1200" height="1026" viewBox="0 0 1200 1026">
    <defs>
      <linearGradient id="band-warm" x1="0" y1="0" x2="0" y2="1">
        <stop offset="0" stop-color="#e5782a"/>
        <stop offset="0.75" stop-color="#eaa02a"/>
        <stop offset="1" stop-color="#ecd81a"/>
      </linearGradient>
      <linearGradient id="band-red" x1="0" y1="0" x2="1" y2="0">
        <stop offset="0" stop-color="#7a1a1e"/>
        <stop offset="0.4" stop-color="#d3363a"/>
        <stop offset="1" stop-color="#e5642c" stop-opacity="0"/>
      </linearGradient>
      <linearGradient id="band-slate" x1="0" y1="0" x2="1" y2="0">
        <stop offset="0" stop-color="#4a4a4a"/>
        <stop offset="0.45" stop-color="#6e6e6e"/>
        <stop offset="1" stop-color="#4c4c4c"/>
      </linearGradient>
      <linearGradient id="site-photo" x1="0" y1="0" x2="0" y2="1">
        <stop offset="0" stop-color="#e8e8e8"/>
        <stop offset="0.6" stop-color="#b9b9b9"/>
        <stop offset="1" stop-color="#d6cdbd"/>
      </linearGradient>
      <linearGradient id="icon-tile" x1="0" y1="0" x2="0" y2="1">
        <stop offset="0" stop-color="#f0a03a"/>
        <stop offset="1" stop-color="#c5560f"/>
      </linearGradient>
    </defs>

    <!-- label base -->
    <rect class="label-base" x="60" y="110" width="1080" height="820" fill="var(--label)"/>

    <!-- construction site photo area -->
    <g role="img" aria-label="Greyscale photo of a construction site with tower cranes, with a golden molecular model in front">
      <polygon points="879,280 1140,262 1140,710 800,730 800,419 763,419" fill="url(#site-photo)"/>
    </g>

    <!-- warm stepped band -->
    <polygon class="band-warm" points="60,110 1140,110 1140,262 879,280 763,419 428,419 281,332 60,332" fill="url(#band-warm)"/>
    <polygon class="band-red" points="60,110 354,110 404,205 60,175" fill="url(#band-red)"/>

    <!-- top slate band -->
    <polygon class="band-slate" points="354,110 1140,110 1140,249 428,249" fill="url(#band-slate)"/>

    <!-- bottom dark band -->
    <polygon class="accent-line" points="420,722 1140,700 1140,708 418,730" fill="var(--orange)"/>
    <polygon class="band-base" points="420,732 1140,710 1140,930 340,930" fill="var(--charcoal)"/>
    <polygon class="accent-red" points="60,860 362,884 359,892 60,868" fill="var(--red)"/>
    <polygon class="accent-red" points="408,732 416,732 338,930 330,930" fill="var(--red)"/>

    <!-- brand mark -->
    <circle cx="265" cy="562" r="78" fill="var(--orange)"/>

    <!-- icon tiles -->
    <g class="icon icon-waterproof">
      <rect x="428" y="778" width="100" height="84" rx="10" fill="url(#icon-tile)"/>
      <path d="M478 790 C470 804 466 810 466 816 a12 12 0 0 0 24 0 c0-6-4-12-12-26z" fill="none" stroke="#fff" stroke-width="3"/>
      <line x1="446" y1="846" x2="510" y2="846" stroke="#fff" stroke-width="3"/>
      <path d="M452 840 l10-8 M468 840 l10-8 M484 840 l10-8 M500 840 l6-5" stroke="#fff" stroke-width="2"/>
    </g>
    <g class="icon icon-brush">
      <rect x="554" y="778" width="100" height="84" rx="10" fill="url(#icon-tile)"/>
      <rect x="599" y="788" width="10" height="30" rx="4" fill="#fff"/>
      <path d="M588 820 h32 v8 c0 12-7 22-16 22 s-16-10-16-22z" fill="#fff"/>
    </g>
    <g class="icon icon-uv">
      <rect x="682" y="778" width="100" height="84" rx="10" fill="url(#icon-tile)"/>
      <circle cx="732" cy="800" r="9" fill="none" stroke="#fff" stroke-width="2.5"/>
      <path d="M732 785 v-4 M732 815 v4 M717 800 h-4 M747 800 h4" stroke="#fff" stroke-width="2.5"/>
      <path d="M700 850 Q732 824 764 850" fill="none" stroke="#fff" stroke-width="3"/>
    </g>
  </svg>

  <p class="tagline">Protective and anti carbonation<br>coating for concrete structures</p>
  <p class="brand">Zorvane<br>Co LLC</p>
  <h1 class="product-name">SEALTEX</h1>
  <p class="product-code">ZX250</p>
  <p class="website">www.zorvane-cc.com</p>
  <p class="net-weight">20<small>kg</small></p>
</div>
</body>
</html>
```